Infection control

to re-design website to include the benefits of powdered bleach packed in pre-measured sachets which when dissolved in water provides economy, efficacy and is safe to use with the use of costly packaging. We need new text outlining the benefits of the world's most commonly used disinfectant for major hospitals, institutions, pathology, military and disaster areas.

Translate design into coded website using CMS with the following features:
Mobile responsive using HTML 5/ CSS3 standards
Coded with SEO standards and with H1 tags for easy spidering and with Wordpress CMS with is page rank 9
Site migration
Email support
Updates

Target Market(s)

hospitals, institutions, pathology, military and disaster areas

Industry/Entity Type

Chemical Product

Number of Pages Required

4 page

Colors

Designer to choose colors to be used in the design.

Requirements
Must have
• factual information based on the efficiency of sodium hypochlorite (bleach) used for infection control. The many viruses, bacteria, pathogens etc which certain strengths of bleach eliminate upon contact.
• As tis is a redesign, existing pages including MSDS sheets to stay the same
Nice to have
• a new look and feel including current logos
Should not have
• incorrect info

```html
<!DOCTYPE html>
<html lang="en">
<head>
<meta charset="utf-8">
<title>Verdaclen – Media &amp; News</title>
<link href="https://fonts.googleapis.com/css2?family=Poppins:wght@400;500;600;700;800&family=Roboto:ital,wght@0,400;0,500;1,400&display=swap" rel="stylesheet">
<style>
:root{
  --green:#6cbd2c;
  --green-dark:#5aa524;
  --green-light:#8fd24d;
  --ink:#2b2b2b;
  --text:#444;
  --muted:#666;
  --card-bg:#f6f6f6;
  --card-line:#e0e0e0;
  --footer-bg:#ececec;
  --white:#fff;
}
*{box-sizing:border-box;margin:0;padding:0}
html,body{width:722px;height:1200px;overflow:hidden;background:var(--white)}
body{position:relative;font-family:"Poppins",sans-serif;color:var(--text)}
.abs{position:absolute}

/* header */
.site-header{position:absolute;left:0;top:0;width:722px;height:73px;background:var(--white)}
.brand{left:58px;top:12px;display:flex;align-items:center;gap:5px}
.brand-mark{width:28px;height:28px;border-radius:50%;border:3px solid var(--green)}
.brand-name{font-size:25px;font-weight:500;color:var(--green);line-height:1}
.brand-tag{left:61px;top:52px;font-size:8px;letter-spacing:.5px;color:#333}
.contact-top{top:13px;display:flex;align-items:center;gap:8px;font-size:10px;color:#333}
.contact-top .ic{width:21px;height:21px;border-radius:50%;border:1.5px solid var(--green);display:flex;align-items:center;justify-content:center}
.nav{font-size:9px;letter-spacing:.4px;color:#222;font-weight:500}
.nav a{position:absolute;white-space:nowrap;text-decoration:none;color:inherit}
.nav a.active{color:var(--green)}

/* hero */
.hero{left:0;top:73px;width:722px;height:228px;background:linear-gradient(100deg,#8bd147 0%,#79c638 50%,#86cc45 100%)}
.hero h1{position:absolute;left:0;width:722px;top:90px;text-align:center;color:var(--white);font-size:29px;font-weight:800;letter-spacing:.5px}
.hero-wave{left:0;top:240px;width:722px;height:62px}

/* news */
.card{position:absolute;top:353px;width:188px;height:320px;background:var(--card-bg);border:1px solid var(--card-line)}
.card .thumb{width:100%;height:125px}
.card h2{font-size:9.4px;font-weight:400;color:#333;text-align:center;margin-top:13px;white-space:nowrap}
.card .meta{display:flex;justify-content:center;gap:14px;margin-top:10px;font-family:"Roboto",sans-serif;font-size:7.4px;font-style:italic;color:var(--green)}
.card p{font-family:"Roboto",sans-serif;font-size:7.4px;line-height:15.5px;text-align:center;color:#444;padding:0 8px;margin-top:9px}

/* benefits */
.benefits-title{left:0;width:722px;top:730px;text-align:center;font-size:21px;font-weight:600;color:var(--ink);letter-spacing:.5px}
.benefit{position:absolute;top:788px;width:110px;text-align:center}
.benefit .ring{width:68px;height:68px;margin:0 auto;border-radius:50%;border:2.5px solid var(--green);display:flex;align-items:center;justify-content:center}
.benefit span{display:block;margin-top:12px;font-family:"Roboto",sans-serif;font-size:10.5px;color:#222}

/* footer */
.footer{left:0;top:950px;width:722px;height:200px;background:var(--footer-bg)}
.footer h3{position:absolute;top:34px;font-size:13.5px;font-weight:500;color:#222;letter-spacing:.5px}
.field{position:absolute;height:26px;width:136px;background:var(--white);border:1px solid #ddd;font-size:7px;color:#333;padding:8px 8px}
.submit{position:absolute;left:59px;top:138px;width:136px;height:24px;background:var(--green);color:var(--white);font-size:9px;font-weight:600;text-align:center;line-height:24px;letter-spacing:.5px}
.info{position:absolute;left:389px;font-size:8px;line-height:13px;color:#333;display:flex;gap:8px}
.links{position:absolute;left:566px;top:78px;list-style:none;font-size:7.5px;color:#222}
.links li{height:13.4px}
.links li::before{content:"›";margin-right:9px;font-size:9px}
.bottom-bar{left:0;top:1150px;width:722px;height:50px;background:var(--white);border-top:1px solid #ddd}
.bottom-brand{left:59px;top:12px;display:flex;align-items:center;gap:3px;font-size:15px;font-weight:500;color:var(--green)}
.bottom-brand i{width:15px;height:15px;border-radius:50%;border:2px solid var(--green)}
.copy{left:0;width:722px;top:17px;text-align:center;font-size:7.5px;color:#333}
.socials{left:598px;top:15px;display:flex;gap:2px}
.socials i{width:15px;height:15px;border-radius:50%;border:1.2px solid #333}
</style>
</head>
<body>

<header class="site-header">
  <div class="abs brand"><i class="brand-mark"></i><span class="brand-name">Verdaclen</span></div>
  <div class="abs brand-tag">Hospital Grade Infection Control</div>

  <div class="abs contact-top" style="left:383px">
    <span class="ic"><svg width="11" height="11" viewBox="0 0 24 24"><path d="M6.6 10.8a15 15 0 0 0 6.6 6.6l2.2-2.2c.3-.3.7-.4 1-.2 1.1.4 2.3.6 3.6.6.6 0 1 .4 1 1V20c0 .6-.4 1-1 1A17 17 0 0 1 3 4c0-.6.4-1 1-1h3.5c.6 0 1 .4 1 1 0 1.3.2 2.5.6 3.6.1.3 0 .7-.2 1z" fill="none" stroke="#6cbd2c" stroke-width="2"/></svg></span>
    1300 555 214
  </div>
  <div class="abs contact-top" style="left:497px">
    <span class="ic"><svg width="11" height="11" viewBox="0 0 24 24"><rect x="3" y="6" width="18" height="12" rx="1" fill="none" stroke="#6cbd2c" stroke-width="2"/><path d="M3 7l9 6 9-6" fill="none" stroke="#6cbd2c" stroke-width="2"/></svg></span>
    info@verdaclen.com
  </div>

  <nav class="abs nav" style="left:0;top:48px;width:722px;height:14px">
    <a style="left:263px">HOME</a>
    <a style="left:306px">ABOUT US</a>
    <a style="left:370px">PRODUCTS</a>
    <a style="left:437px">DOWNLOADS</a>
    <a class="active" style="left:514px">MEDIA &amp; NEWS</a>
    <a style="left:600px">CONTACT US</a>
  </nav>
</header>

<section class="abs hero" role="img" aria-label="Smiling doctor and nurse in a hospital, green tinted photograph">
  <h1>MEDIA &amp; NEWS</h1>
</section>
<svg class="abs hero-wave" viewBox="0 0 722 62" preserveAspectRatio="none">
  <path d="M0 62 L0 38 C120 0 250 10 400 40 C520 62 640 45 722 22 L722 62 Z" fill="#fff"/>
  <path d="M0 38 C120 0 250 10 400 40 C300 14 150 6 0 30 Z" fill="#a9df6e"/>
</svg>

<main>
  <article class="card" style="left:59px">
    <div class="thumb" role="img" aria-label="Gloved hand holding a molecular model" style="background:linear-gradient(120deg,#3f6fa8,#9fbfe0 50%,#d8e4f0)"></div>
    <h2>About Sodium Hypochlorite</h2>
    <div class="meta"><span>▦ March 25, 2018</span><span>○ No comments</span></div>
    <p>Sed ut perspiciatis unde omnis iste natus error sit voluptatem accusantium doloremque ludantium, totam rem aperiam, eaque ipsa quae ab illo inventore veritatis et quasi ahitecto beatae vitae dicta sunt explicabo. Nemo enim ipsam voluptatem quia voluptas sit aspernatur aut odit aut fugit, sed quia cnsequuntur magni dolores</p>
  </article>
  <article class="card" style="left:267px">
    <div class="thumb" role="img" aria-label="Microscopic view of virus particles" style="background:radial-gradient(circle at 55% 60%,#2c7f95,#4a1c2a 55%,#8c2a3a)"></div>
    <h2>National Infection Prevention Guidelines</h2>
    <div class="meta"><span>▦ March 25, 2018</span><span>○ No comments</span></div>
    <p>Sed ut perspiciatis unde omnis iste natus error sit voluptatem accusantium doloremque ludantium, totam rem aperiam, eaque ipsa quae ab illo inventore veritatis et quasi ahitecto beatae vitae dicta sunt explicabo. Nemo enim ipsam voluptatem quia voluptas sit aspernatur aut odit aut fugit, sed quia cnsequuntur magni dolores</p>
  </article>
  <article class="card" style="left:473px">
    <div class="thumb" role="img" aria-label="Doctor touching a medical interface with the words HCPA Advert" style="background:linear-gradient(110deg,#e8eef6,#c7d3e4 60%,#f2f4f8)"></div>
    <h2>HCPA Advert</h2>
    <div class="meta"><span>▦ March 25, 2018</span><span>○ No comments</span></div>
    <p>Sed ut perspiciatis unde omnis iste natus error sit voluptatem accusantium doloremque ludantium, totam rem aperiam, eaque ipsa quae ab illo inventore veritatis et quasi ahitecto beatae vitae dicta sunt explicabo. Nemo enim ipsam voluptatem quia voluptas sit aspernatur aut odit aut fugit, sed quia cnsequuntur magni dolores</p>
  </article>

  <h2 class="abs benefits-title">VERDACLEN BENEFITS</h2>

  <div class="benefit" style="left:87px">
    <div class="ring"><svg width="36" height="36" viewBox="0 0 36 36" fill="none" stroke="#6cbd2c" stroke-width="1.8"><rect x="5" y="9" width="16" height="22"/><rect x="21" y="17" width="10" height="14"/><path d="M9 13h3M14 13h3M9 18h3M14 18h3M9 23h3M14 23h3M24 21h4M24 25h4M11 31v-4h4v4M10 5h6v4h-6z"/></svg></div>
    <span>HOSPITALS</span>
  </div>
  <div class="benefit" style="left:195px">
    <div class="ring"><svg width="34" height="34" viewBox="0 0 34 34" fill="#6cbd2c"><path d="M17 4 L31 11 H3 Z"/><rect x="5" y="13" width="3" height="12"/><rect x="11" y="13" width="3" height="12"/><rect x="20" y="13" width="3" height="12"/><rect x="26" y="13" width="3" height="12"/><rect x="3" y="26" width="28" height="4"/></svg></div>
    <span>INSTITUTIONS</span>
  </div>
  <div class="benefit" style="left:303px">
    <div class="ring"><svg width="34" height="34" viewBox="0 0 34 34" fill="#6cbd2c"><rect x="13" y="3" width="5" height="14" rx="1"/><circle cx="20" cy="17" r="4"/><path d="M22 14a9 9 0 0 1-2 14h-10v3h16v-3h-2a12 12 0 0 0 0-16z"/><rect x="9" y="20" width="8" height="3"/></svg></div>
    <span>PATHOLOGY</span>
  </div>
  <div class="benefit" style="left:411px">
    <div class="ring"><svg width="34" height="34" viewBox="0 0 34 34" fill="none" stroke="#6cbd2c" stroke-width="1.8"><path d="M9 14a8 8 0 0 1 16 0z"/><path d="M7 14h20"/><path d="M6 31v-5a5 5 0 0 1 5-5h12a5 5 0 0 1 5 5v5z"/><path d="M10 27h14"/></svg></div>
    <span>MILITARY</span>
  </div>
  <div class="benefit" style="left:519px">
    <div class="ring"><svg width="28" height="32" viewBox="0 0 28 32"><path d="M14 2a10 10 0 0 0-10 10c0 8 10 18 10 18s10-10 10-18A10 10 0 0 0 14 2z" fill="#6cbd2c"/><circle cx="14" cy="12" r="4" fill="#fff"/></svg></div>
    <span>DISASTER AREAS</span>
  </div>
</main>

<footer class="abs footer">
  <h3 style="left:59px">GET A QUICK NOW!</h3>
  <h3 style="left:389px">CONTACT US</h3>
  <h3 style="left:566px">QUICK LINK</h3>

  <div class="field" style="left:59px;top:72px">Your Name</div>
  <div class="field" style="left:203px;top:72px">Your E - Mail</div>
  <div class="field" style="left:59px;top:103px">Your Phone</div>
  <div class="field" style="left:203px;top:103px">Message</div>
  <div class="submit">SUBMIT</div>

  <div class="info" style="top:75px"><svg width="8" height="10" viewBox="0 0 28 32"><path d="M14 2a10 10 0 0 0-10 10c0 8 10 18 10 18s10-10 10-18A10 10 0 0 0 14 2z" fill="#6cbd2c"/><circle cx="14" cy="12" r="4" fill="#ececec"/></svg><span>Harbor Supply P.O. Box 4410<br>Newton, CT 06470</span></div>
  <div class="info" style="top:108px"><svg width="9" height="9" viewBox="0 0 24 24"><path d="M6.6 10.8a15 15 0 0 0 6.6 6.6l2.2-2.2c.3-.3.7-.4 1-.2 1.1.4 2.3.6 3.6.6.6 0 1 .4 1 1V20c0 .6-.4 1-1 1A17 17 0 0 1 3 4c0-.6.4-1 1-1h3.5c.6 0 1 .4 1 1 0 1.3.2 2.5.6 3.6.1.3 0 .7-.2 1z" fill="#6cbd2c"/></svg><span style="font-size:8.5px">Phone:1300 555 214<br>Fax : 1300 555 215</span></div>
  <div class="info" style="top:133px"><svg width="9" height="9" viewBox="0 0 24 24"><rect x="2" y="5" width="20" height="14" fill="#6cbd2c"/><path d="M2 6l10 7 10-7" fill="none" stroke="#ececec" stroke-width="2"/></svg><span>info@verdaclen.com</span></div>

  <ul class="links">
    <li>Home</li><li>About</li><li>Products</li><li>Downloads</li><li>Media &amp; News</li><li>Contact Us</li>
  </ul>
</footer>

<div class="abs bottom-bar">
  <div class="abs bottom-brand"><i></i>Verdaclen</div>
  <div class="abs copy">©2018 Verdaclen. All Rights Reserved</div>
  <div class="abs socials"><i></i><i></i><i></i><i></i></div>
</div>

</body>
</html>
```